Website Design - Financial Services Software

We are looking for website designs for our public website.
Some competitor sites we like are
www.torvani.com.au
www.pluma.com.au
www.quentabridge.com
www.morlupa.com.au

A wireframe example of our site can be found at
http://pr4tqz.bivlowpage.com/

Attached is our logo.

Industry/Entity Type

Financial

```html
<!DOCTYPE html>
<html lang="en">
<head>
<meta charset="utf-8">
<title>Veltora — Smarter Financial Strategies</title>
<link rel="stylesheet" href="https://fonts.googleapis.com/css2?family=Oswald:wght@300;400;500&family=Arimo:wght@400;700&display=swap">
<style>
:root{
  --ink:#1c1c1c;
  --dark:#191919;
  --bar:#222222;
  --gold:#b07a26;
  --navy:#0f2f4f;
  --blue-light:#3a8fd0;
  --paper:#ffffff;
  --mist:#f1f1f1;
  --slate:#3d4650;
  --footer:#3a3b3d;
  --footer-deep:#262626;
  --body-font:"Arimo",Arial,sans-serif;
  --head-font:"Oswald","Arial Narrow",sans-serif;
}
*{box-sizing:border-box;margin:0;padding:0}
html,body{width:1200px;height:2332px;overflow:hidden;background:var(--paper);font-family:var(--body-font);color:var(--ink)}
.page{position:relative;width:1200px;height:2332px}
.abs{position:absolute}

/* top strip */
.top-strip{left:0;top:0;width:1200px;height:30px;background:var(--bar)}
.top-links{left:174px;top:8px;font:400 11px var(--head-font);color:#ddd;letter-spacing:.5px}
.top-links span{margin:0 5px}
.login{left:325px;top:2px;width:58px;height:26px;background:var(--gold);color:#fff;font:400 11px var(--head-font);text-align:center;line-height:26px}
.social{left:905px;top:6px;display:flex;gap:5px}
.social i{display:block;width:16px;height:16px;background:#6c6c6c;border-radius:2px}

/* hero */
.hero{left:0;top:30px;width:1200px;height:558px;background:linear-gradient(180deg,#ffffff 0%,#f4f4f5 55%,#e3e3e6 100%)}
.brand{left:172px;top:112px;width:190px;text-align:center}
.brand-mark{display:block;width:22px;height:22px;margin:0 auto 10px;border-radius:50%;background:var(--gold)}
.brand-name{font:500 38px/1 var(--head-font);color:var(--gold);letter-spacing:2px;text-transform:uppercase}
.brand-tag{font:400 10px var(--body-font);color:var(--navy);margin-top:8px;letter-spacing:1px;text-transform:uppercase}
.nav{top:64px;font:400 14px var(--head-font);color:#777;letter-spacing:.5px}
.nav.active{color:var(--ink)}
.nav-marker{left:470px;top:30px;width:86px;height:3px;background:var(--gold)}
.dropdown{left:421px;top:158px;width:140px;background:#fff;box-shadow:0 2px 6px rgba(0,0,0,.15);font:700 11px var(--body-font)}
.dropdown div{padding:7px 16px;color:#999;border-top:1px solid #eee}
.dropdown div:first-child{color:var(--ink);border-top:0}
.hero-title{left:158px;top:248px;font:400 27px var(--head-font);color:var(--navy)}
.hero-sub{left:158px;top:290px;width:330px;font:400 17px/24px var(--body-font);color:var(--gold)}
.hero-photo{left:60px;top:340px;width:320px;height:200px;background:linear-gradient(180deg,rgba(228,228,231,0) 0%,rgba(214,214,218,.6) 100%)}
.btn{display:flex;align-items:center;justify-content:space-between;font:500 15px var(--head-font);color:#fff;padding:0 14px}
.btn-dark{background:#2b2118}
.btn-gold{background:var(--gold)}
.chev{width:8px;height:12px}
.video{left:531px;top:212px;width:529px;height:296px;background:linear-gradient(180deg,#6f8fb1 0%,#a7bccf 45%,#7fa05a 80%,#5a7c3c 100%);border:2px solid #333}

/* features */
.features{left:0;top:588px;width:1200px;height:955px;background:var(--dark)}
.photo-frame{left:147px;top:678px;width:310px;height:230px;border:6px solid var(--gold);background:linear-gradient(135deg,#c9cbc4 0%,#8c8f86 50%,#4d4b44 100%)}
.feature .icon{width:36px;height:36px;display:block}
.feature h3{font:300 18px var(--head-font);color:var(--blue-light);margin:6px 0 4px}
.feature p{width:228px;font:400 13.5px/21px var(--body-font);color:#eee}
.more{display:inline-flex;align-items:center;gap:6px;margin-top:16px;height:20px;padding:0 10px;background:var(--navy);border-radius:10px;font:400 9px var(--body-font);color:#fff}
.more svg{width:5px;height:8px}
.about{left:158px;top:960px;width:280px}
.about h2{display:flex;align-items:center;gap:12px;font:400 27px var(--head-font);color:var(--blue-light)}
.about p{font:400 13.5px/20.5px var(--body-font);color:#eee;margin-top:6px}
.about hr{border:0;border-top:1px solid #bbb;margin-top:14px}
.pricing{left:170px;top:1369px;width:259px;height:64px;font:400 27px var(--head-font);letter-spacing:.5px;padding:0 22px}

/* trial */
.divider{left:158px;top:1575px;width:915px;height:1px;background:#ddd}
.divider-dot{left:602px;top:1562px;width:26px;height:26px;border-radius:50%;border:1px solid #ccc;background:#fff}
.trial{left:158px;top:1609px;width:915px;height:120px;background:var(--mist);border:1px solid #e6e6e6}
.trial-text{left:183px;top:1648px;font:400 30px var(--head-font);color:var(--ink)}
.tour{left:797px;top:1638px;width:256px;height:61px;background:#1c1c1c;font:400 26px var(--head-font);letter-spacing:2px;padding:0 22px}

/* blog */
.blog-tag{left:158px;top:1776px;width:104px;height:25px;background:var(--gold);color:#fff;font:400 11px var(--head-font);text-align:center;line-height:25px}
.blog{left:0;top:1801px;width:1200px;height:144px;background:var(--slate);border-top:4px solid #4a3220;border-bottom:5px solid var(--gold)}
.thumb{width:104px;height:78px;border:3px solid #222}
.post{font:400 12px/17px var(--body-font);color:#fff}
.post .link{color:var(--blue-light);font-size:14px}
.post .by{font:400 15px var(--head-font);margin-top:2px}

/* footer */
.footer{left:0;top:1950px;width:1200px;height:382px;background:var(--footer)}
.footer-brand{left:126px;top:1986px;width:226px;height:188px;background:#000;border:5px solid #2c2c2c;text-align:center;padding-top:56px}
.footer-brand .brand-mark{background:#fff}
.footer-brand .brand-name{color:#fff;font-size:30px}
.footer-brand .brand-tag{color:#fff;font-size:8px}
.fcol{top:2016px;font:400 11px var(--body-font);color:#fff}
.fcol h4{font:400 12px var(--head-font);width:86px;padding-bottom:6px;border-bottom:1px solid #666;margin-bottom:10px;letter-spacing:.5px}
.fcol li{list-style:none;font-weight:700;font-size:10px;line-height:28px;display:flex;align-items:center;gap:8px}
.fcol li i{display:block;width:11px;height:11px;background:#ddd}
.copy{left:158px;top:2216px;font:400 10px var(--body-font);color:#ccc}
.base{left:36px;top:2282px;width:1128px;height:50px;background:var(--footer-deep)}
.base-links{left:65px;top:2298px;font:700 10px var(--body-font);color:#fff}
.base-links span{margin:0 4px}
.base-brand{left:1000px;top:2290px;text-align:left}
.base-brand .brand-name{font-size:21px;color:#fff}
.base-brand .brand-tag{font-size:6px;color:#ccc;margin-top:3px}
</style>
</head>
<body>
<div class="page">

  <!-- top strip -->
  <div class="abs top-strip"></div>
  <div class="abs top-links">ABOUT <span>|</span> PRICING <span>|</span> SERVICES</div>
  <div class="abs login">LOGIN</div>
  <div class="abs social"><i></i><i></i><i></i><i></i><i></i></div>

  <!-- hero -->
  <div class="abs hero"></div>
  <div class="abs hero-photo" role="img" aria-label="Computer mouse on a light desk"></div>
  <div class="abs brand">
    <span class="brand-mark"></span>
    <div class="brand-name">Veltora</div>
    <div class="brand-tag">Smarter Financial Strategies</div>
  </div>
  <div class="abs nav-marker"></div>
  <div class="abs nav active" style="left:484px">FEATURES</div>
  <div class="abs nav" style="left:606px">EXAMPLES</div>
  <div class="abs nav" style="left:739px">FAQ</div>
  <div class="abs nav" style="left:861px">ABOUT</div>
  <div class="abs dropdown">
    <div>Lorem Ipsum</div>
    <div>Lorem Ipsum</div>
    <div>Lorem Ipsum</div>
  </div>
  <h1 class="abs hero-title">Smarter Financial Strategies</h1>
  <p class="abs hero-sub">Values and Cash-flow focused financial software for financial planners.</p>
  <a class="abs btn btn-dark" style="left:115px;top:499px;width:186px;height:54px">For Planning Practices
    <svg class="chev" viewBox="0 0 8 12"><path d="M1 1l5 5-5 5" fill="none" stroke="#fff" stroke-width="2"/></svg></a>
  <a class="abs btn btn-gold" style="left:314px;top:499px;width:185px;height:54px">For Dealer Groups
    <svg class="chev" viewBox="0 0 8 12"><path d="M1 1l5 5-5 5" fill="none" stroke="#fff" stroke-width="2"/></svg></a>
  <div class="abs video" role="img" aria-label="Introductory video with an animated presenter and company title card"></div>

  <!-- features -->
  <div class="abs features"></div>
  <div class="abs photo-frame" role="img" aria-label="Training session with people at laptops in a classroom"></div>

  <div class="abs feature" style="left:486px;top:650px">
    <svg class="icon" viewBox="0 0 36 36"><circle cx="18" cy="14" r="9" fill="none" stroke="#b07a26" stroke-width="2.5"/><path d="M14 23v5h8v-5M15 31h6" fill="none" stroke="#b07a26" stroke-width="2.5"/></svg>
    <h3>Smart Idea</h3>
    <p>Lorem ipsum dolor sit amet, consectetur adipiscing elit, sed ipsum dolor sit amet, consectetur adipiscing elit, sed do eiusmod tempor adipiscing.</p>
    <span class="more">Learn more <svg viewBox="0 0 5 8"><path d="M1 1l3 3-3 3" fill="none" stroke="#fff" stroke-width="1.4"/></svg></span>
  </div>
  <div class="abs feature" style="left:771px;top:648px">
    <svg class="icon" viewBox="0 0 36 36"><circle cx="18" cy="18" r="15" fill="none" stroke="#b07a26" stroke-width="2.5"/><circle cx="18" cy="18" r="7" fill="#b07a26"/></svg>
    <h3>Web Strategy</h3>
    <p>Lorem ipsum dolor sit amet, consectetur adipiscing elit, sed ipsum dolor sit amet, consectetur adipiscing elit, sed do eiusmod tempor adipiscing.</p>
    <span class="more">Learn more <svg viewBox="0 0 5 8"><path d="M1 1l3 3-3 3" fill="none" stroke="#fff" stroke-width="1.4"/></svg></span>
  </div>

  <section class="abs about">
    <h2><svg width="36" height="40" viewBox="0 0 36 40"><circle cx="18" cy="11" r="9" fill="#b07a26"/><path d="M2 40c0-12 7-18 16-18s16 6 16 18z" fill="#b07a26"/></svg>About Us</h2>
    <p>Lorem ipsum dolor sit amet, consectetur adipiscing elit. Morbi dapibus justo vel felis volutpat, sit amet congue arcu lacinia. Aenean elementum hendrerit turpis nec sodales.<br>Maecenas vehicula justo et mauris tempus, vel dignissim dolor aliquet. Maecenas erat metus, scelerisque eget placerat gravida, consectetur fermentum magna.</p>
    <hr>
  </section>

  <div class="abs feature" style="left:486px;top:956px">
    <svg class="icon" viewBox="0 0 36 36" style="width:62px;height:50px"><path d="M2 8h12l3 4h17v20H2z" fill="#b07a26"/></svg>
    <h3>Directory Submition</h3>
    <p>Lorem ipsum dolor sit amet, consectetur adipiscing elit, sed ipsum dolor sit amet, consectetur adipiscing elit, sed do eiusmod tempor adipiscing.</p>
    <span class="more">Learn more <svg viewBox="0 0 5 8"><path d="M1 1l3 3-3 3" fill="none" stroke="#fff" stroke-width="1.4"/></svg></span>
  </div>
  <div class="abs feature" style="left:771px;top:951px">
    <svg class="icon" viewBox="0 0 36 36" style="width:48px;height:48px"><rect x="3" y="3" width="13" height="13" fill="none" stroke="#b07a26" stroke-width="3"/><rect x="20" y="3" width="13" height="13" fill="#b07a26"/><rect x="3" y="20" width="13" height="13" fill="#b07a26"/><rect x="20" y="20" width="13" height="13" fill="none" stroke="#b07a26" stroke-width="3"/></svg>
    <h3>Office Software</h3>
    <p>Lorem ipsum dolor sit amet, consectetur adipiscing elit, sed ipsum dolor sit amet, consectetur adipiscing elit, sed do eiusmod tempor adipiscing.</p>
    <span class="more">Learn more <svg viewBox="0 0 5 8"><path d="M1 1l3 3-3 3" fill="none" stroke="#fff" stroke-width="1.4"/></svg></span>
  </div>

  <a class="abs btn btn-gold pricing">Painless pricing
    <svg class="chev" viewBox="0 0 8 12"><path d="M1 1l5 5-5 5" fill="none" stroke="#fff" stroke-width="2"/></svg></a>

  <div class="abs feature" style="left:521px;top:1265px">
    <svg class="icon" viewBox="0 0 36 36"><path d="M2 34v-8h8v-8h8v-8h8V2h8" fill="none" stroke="#b07a26" stroke-width="4"/></svg>
  </div>
  <div class="abs feature" style="left:486px;top:1318px">
    <h3>Manage Your Workflow</h3>
    <p>Lorem ipsum dolor sit amet, consectetur adipiscing elit, sed ipsum dolor sit amet, consectetur adipiscing elit, sed do eiusmod tempor adipiscing.</p>
    <span class="more">Learn more <svg viewBox="0 0 5 8"><path d="M1 1l3 3-3 3" fill="none" stroke="#fff" stroke-width="1.4"/></svg></span>
  </div>
  <div class="abs feature" style="left:786px;top:1263px">
    <svg class="icon" viewBox="0 0 36 36" style="width:44px;height:44px"><circle cx="13" cy="13" r="7" fill="none" stroke="#b07a26" stroke-width="5" stroke-dasharray="3 2"/><circle cx="25" cy="25" r="7" fill="none" stroke="#b07a26" stroke-width="5" stroke-dasharray="3 2"/></svg>
  </div>
  <div class="abs feature" style="left:771px;top:1311px">
    <h3>Customisable fact finding</h3>
    <p>Lorem ipsum dolor sit amet, consectetur adipiscing elit, sed ipsum dolor sit amet, consectetur adipiscing elit, sed do eiusmod tempor adipiscing.</p>
    <span class="more">Learn more <svg viewBox="0 0 5 8"><path d="M1 1l3 3-3 3" fill="none" stroke="#fff" stroke-width="1.4"/></svg></span>
  </div>

  <!-- trial -->
  <div class="abs divider"></div>
  <div class="abs divider-dot"></div>
  <div class="abs trial"></div>
  <p class="abs trial-text">Create an account today and begin your 30 day trial!</p>
  <a class="abs btn tour">TAKE A TOUR
    <svg class="chev" viewBox="0 0 8 12"><path d="M1 1l5 5-5 5" fill="none" stroke="#fff" stroke-width="1.6"/></svg></a>

  <!-- blog -->
  <div class="abs blog-tag">LATEST FROM BLOG</div>
  <div class="abs blog"></div>
  <div class="abs thumb" style="left:158px;top:1830px;background:linear-gradient(135deg,#9fb3c4,#556270)" role="img" aria-label="Business team meeting"></div>
  <div class="abs post" style="left:271px;top:1826px">
    <div>4 Feb 2014</div><div>lorem Ipsum</div>
    <div class="link">Lorem Ipsum Dolor Sit Amet</div>
    <div class="by">by Mr. Hale</div>
  </div>
  <div class="abs thumb" style="left:615px;top:1830px;background:linear-gradient(135deg,#e6e8ea,#8c939a)" role="img" aria-label="Presenter at a whiteboard"></div>
  <div class="abs post" style="left:725px;top:1826px">
    <div>3 Feb 2014</div><div>lorem Ipsum</div>
    <div class="link">Lorem Ipsum Dolor Sit Amet</div>
    <div class="by">by Mr. Ames</div>
  </div>

  <!-- footer -->
  <div class="abs footer"></div>
  <div class="abs footer-brand">
    <span class="brand-mark"></span>
    <div class="brand-name">Veltora</div>
    <div class="brand-tag">Smarter Financial Strategies</div>
  </div>
  <div class="abs fcol" style="left:384px"><h4>ABOUT</h4><ul><li>About us</li><li>Support</li></ul></div>
  <div class="abs fcol" style="left:553px"><h4>GETING STARTED</h4><ul><li>Why Veltora</li><li>Download a Summary</li><li>Veltora Videos</li></ul></div>
  <div class="abs fcol" style="left:762px"><h4>LEGAL</h4><ul><li>Terms of Use</li><li>Privacy</li></ul></div>
  <div class="abs fcol" style="left:953px"><h4>CONNECT</h4><ul><li><i></i>Veltora on Netlinker</li><li><i></i>Veltora on Chirpline</li></ul></div>
  <p class="abs copy">Copyright © 2014 Veltora Pty Ltd. All rights reserved.</p>

  <div class="abs base"></div>
  <div class="abs base-links">Home <span>|</span> About <span>|</span> FAQ <span>|</span> Services <span>|</span> Contact <span>|</span></div>
  <div class="abs base-brand">
    <div class="brand-name">Veltora</div>
    <div class="brand-tag">Smarter Financial Strategies</div>
  </div>

</div>
</body>
</html>
```